Red Mesa Stewardship Summit needs a marketing flyer

We need a full page graphic for our upcoming Forum that can also be converted into a website "header" for social media, etc.: "Red Mesa Stewardship Summit - Making Impact Through the Built Environment"

INTRODUCTION:
During the first week of August 2022, Q-TarVN is presenting the Red Mesa Stewardship Summit - Making Impact Through the Built Environment.

One of the most exciting aspects of this conference will be the bringing together of multiple organizations including for-profits and nonprofits, K-12’s and higher education, cities and counties and other governmental agencies, as well as architects, engineers, and contractors to collaboratively present and discuss issues and ideas related to sustainability, with a Texas focus.

This event will be a catalyst for public and private project owners to holistically gather information and momentum as we bring the resources and vision needed to achieve the goal of zero carbon emissions from the built environment by 2040, and address water, green space and the natural environment, transportation, equity, and funding, among other topics.

```html
<!DOCTYPE html>
<html lang="en">
<head>
<meta charset="utf-8">
<title>Red Mesa Stewardship Summit – Flyer</title>
<link href="https://fonts.googleapis.com/css2?family=Montserrat:ital,wght@0,500;0,600;0,700;0,800;1,700&display=swap" rel="stylesheet">
<style>
  :root{
    --blue:#3a53a4;
    --blue-dark:#2c3f87;
    --green:#8cb43f;
    --green-dark:#6f9a2a;
    --charcoal:#3b3b3d;
    --ink:#1f1f22;
    --rule:#c9ccd3;
    --paper:#ffffff;
    --stage:#f1f1f1;
  }
  *{margin:0;padding:0;box-sizing:border-box}
  html,body{width:1200px;height:2492px;overflow:hidden}
  body{background:var(--stage);font-family:"Montserrat",Arial,sans-serif;color:var(--ink);position:relative}
  .flyer{position:absolute;left:0;top:446px;width:1200px;height:1600px;background:var(--paper);overflow:hidden}
  .flyer-art{position:absolute;inset:0}
  .title{position:absolute;left:0;width:1200px;text-align:center;color:#fff;font-weight:800;line-height:1;letter-spacing:-1px}
  .title-line1{top:692px;font-size:62px}
  .title-line2{top:762px;font-size:80px}
  .title-line3{top:842px;font-size:98px}
  .tagline{position:absolute;top:1004px;left:0;width:1200px;text-align:center;color:var(--green);font-weight:800;font-size:39px;letter-spacing:-.5px}
  .date-block{position:absolute;left:88px;top:1062px;height:80px;display:flex;gap:8px}
  .date-lead{background:var(--blue);color:#fff;border-radius:6px 0 0 6px;display:flex;align-items:center;padding:0 14px 0 18px;gap:14px}
  .date-lead small{font-size:25px;font-weight:600;line-height:1.1}
  .date-lead strong{font-size:54px;font-weight:700;letter-spacing:-1px}
  .date-year{background:var(--charcoal);color:#fff;border-radius:0 6px 6px 0;font-size:58px;font-weight:700;display:flex;align-items:center;padding:0 12px;letter-spacing:-1px}
  .story{position:absolute;left:88px;top:1156px;width:630px;display:flex;flex-direction:column;gap:8px}
  .intro{font-size:20px;font-weight:600;line-height:1.26;letter-spacing:-.2px}
  .intro-highlight{font-size:20px;font-weight:700;font-style:italic;color:var(--blue);line-height:1.26;letter-spacing:-.2px}
  .audience-grid{display:grid;grid-template-columns:305px 325px;margin-top:10px}
  .audience{list-style:none;font-size:17px;font-weight:500;line-height:1.25}
  .audience li{position:relative;padding-left:26px;margin-bottom:12px}
  .audience-left{padding-top:10px}
  .tick{position:absolute;left:0;top:2px;width:16px;height:16px}
  .vision-card{position:absolute;left:733px;top:1065px;width:380px;height:408px;border:2px solid var(--blue);border-radius:10px;background:#f4f5f8}
  .vision-tab{position:absolute;left:-2px;top:10px;width:82px;height:386px;background:var(--green);border-radius:0 40px 40px 0}
  .vision-eye{position:absolute;left:20px;top:70px;width:44px;height:44px}
  .vision-label{position:absolute;left:18px;top:320px;transform:rotate(-90deg);transform-origin:left top;color:#fff;font-weight:700;font-size:46px;letter-spacing:1px}
  .vision-goal{position:absolute;left:104px;top:40px;width:262px;font-size:18.5px;font-weight:500;line-height:1.2}
  .vision-goal span{color:var(--blue)}
  .vision-topics{position:absolute;left:100px;top:152px;width:262px;list-style:none;font-size:18px;font-weight:500}
  .vision-topics li{position:relative;padding:6px 0 7px 50px;border-bottom:1px solid var(--rule)}
  .vision-topics li:last-child{border-bottom:none}
  .vision-topics .tick{left:4px;top:9px}
  .footer-rule{position:absolute;left:75px;top:1494px;width:1037px;height:2px;background:var(--rule)}
  .footer{position:absolute;left:80px;top:1510px;width:1040px;height:60px;display:flex;align-items:center;font-weight:500;font-size:27px;color:var(--ink)}
  .brand{display:flex;align-items:center;gap:12px;margin-right:36px}
  .brand-dot{width:50px;height:50px;border-radius:50%;background:var(--blue)}
  .brand-name{font-size:32px;font-weight:600;color:var(--charcoal)}
  .contact{display:flex;align-items:center;gap:5px;margin-right:16px}
  .contact svg{width:22px;height:22px}
</style>
</head>
<body>
<main class="flyer">
  <svg class="flyer-art" viewBox="0 0 1200 1600" width="1200" height="1600">
    <defs>
      <radialGradient id="forestLight" cx="0.52" cy="0.32" r="0.7">
        <stop offset="0" stop-color="#fff6b0"/>
        <stop offset="0.18" stop-color="#d9d23a"/>
        <stop offset="0.45" stop-color="#6e9a24"/>
        <stop offset="0.8" stop-color="#3d6b18"/>
        <stop offset="1" stop-color="#2a4e12"/>
      </radialGradient>
      <clipPath id="photoClip"><circle cx="600" cy="300" r="690"/></clipPath>
    </defs>
    <rect x="0" y="560" width="1200" height="520" fill="var(--green)"/>
    <path d="M0,1060 Q300,900 600,900 Q900,900 1200,1060 V1600 H0 Z" fill="#fff"/>
    <g clip-path="url(#photoClip)">
      <rect x="0" y="0" width="1200" height="1000" fill="url(#forestLight)" role="img" aria-label="Photo of a sunlit green forest with a hand holding up a light bulb, ringed by white sustainability icons"/>
    </g>
    <circle cx="600" cy="300" r="690" fill="none" stroke="#fff" stroke-width="4"/>
    <ellipse cx="600" cy="808" rx="470" ry="186" fill="var(--blue)" stroke="#fff" stroke-width="4"/>
    <path d="M1150,1600 L1200,1540 V1600 Z" fill="var(--green)"/>
  </svg>

  <h1>
    <span class="title title-line1">RED MESA</span>
    <span class="title title-line2">STEWARDSHIP</span>
    <span class="title title-line3">SUMMIT</span>
  </h1>

  <p class="tagline">Making Impact Through the Built Environment</p>

  <div class="date-block">
    <div class="date-lead"><small>During the<br>first week of</small><strong>AUGUST</strong></div>
    <div class="date-year">2022</div>
  </div>

  <div class="story">
    <p class="intro">Q-TarVN is presenting the Red Mesa Stewardship Summit Making Impact Through the Built Environment.</p>
    <p class="intro-highlight">One of the most exciting aspects of this conference will be the bringing together of multiple organizations including for-</p>
    <div class="audience-grid">
      <ul class="audience audience-left">
        <li><svg class="tick" viewBox="0 0 16 16"><circle cx="8" cy="8" r="6.5" fill="none" stroke="var(--green)" stroke-width="1.6"/><path d="M5 8.2l2 2 4-4" fill="none" stroke="var(--green)" stroke-width="1.6"/></svg>Profits and nonprofits,</li>
        <li><svg class="tick" viewBox="0 0 16 16"><circle cx="8" cy="8" r="6.5" fill="none" stroke="var(--green)" stroke-width="1.6"/><path d="M5 8.2l2 2 4-4" fill="none" stroke="var(--green)" stroke-width="1.6"/></svg>K-12’s and higher education,</li>
        <li><svg class="tick" viewBox="0 0 16 16"><circle cx="8" cy="8" r="6.5" fill="none" stroke="var(--green)" stroke-width="1.6"/><path d="M5 8.2l2 2 4-4" fill="none" stroke="var(--green)" stroke-width="1.6"/></svg>Cities and counties and other governmental agencies,</li>
      </ul>
      <ul class="audience audience-right">
        <li><svg class="tick" viewBox="0 0 16 16"><circle cx="8" cy="8" r="6.5" fill="none" stroke="var(--green)" stroke-width="1.6"/><path d="M5 8.2l2 2 4-4" fill="none" stroke="var(--green)" stroke-width="1.6"/></svg>Architects &amp; engineers,</li>
        <li><svg class="tick" viewBox="0 0 16 16"><circle cx="8" cy="8" r="6.5" fill="none" stroke="var(--green)" stroke-width="1.6"/><path d="M5 8.2l2 2 4-4" fill="none" stroke="var(--green)" stroke-width="1.6"/></svg>Contractors to collaboratively present and discuss issues and ideas related to sustainability, with a Texas focus.</li>
      </ul>
    </div>
  </div>

  <section class="vision-card">
    <div class="vision-tab">
      <svg class="vision-eye" viewBox="0 0 44 44"><path d="M4 22 Q22 6 40 22 Q22 38 4 22Z" fill="none" stroke="#fff" stroke-width="3"/><circle cx="22" cy="22" r="6" fill="#fff"/><path d="M22 4v5M10 8l3 4M34 8l-3 4" stroke="#fff" stroke-width="3"/></svg>
      <span class="vision-label">VISION</span>
    </div>
    <p class="vision-goal">Achieve the goal of zero carbon emissions from the <span>built environment by 2040.</span></p>
    <ul class="vision-topics">
      <li><svg class="tick" viewBox="0 0 16 16"><circle cx="8" cy="8" r="6.5" fill="none" stroke="var(--green)" stroke-width="1.6"/><path d="M5 8.2l2 2 4-4" fill="none" stroke="var(--green)" stroke-width="1.6"/></svg>Address water</li>
      <li><svg class="tick" viewBox="0 0 16 16"><circle cx="8" cy="8" r="6.5" fill="none" stroke="var(--green)" stroke-width="1.6"/><path d="M5 8.2l2 2 4-4" fill="none" stroke="var(--green)" stroke-width="1.6"/></svg>Green space and the</li>
      <li><svg class="tick" viewBox="0 0 16 16"><circle cx="8" cy="8" r="6.5" fill="none" stroke="var(--green)" stroke-width="1.6"/><path d="M5 8.2l2 2 4-4" fill="none" stroke="var(--green)" stroke-width="1.6"/></svg>Natural environment,</li>
      <li><svg class="tick" viewBox="0 0 16 16"><circle cx="8" cy="8" r="6.5" fill="none" stroke="var(--green)" stroke-width="1.6"/><path d="M5 8.2l2 2 4-4" fill="none" stroke="var(--green)" stroke-width="1.6"/></svg>Transportation,</li>
      <li><svg class="tick" viewBox="0 0 16 16"><circle cx="8" cy="8" r="6.5" fill="none" stroke="var(--green)" stroke-width="1.6"/><path d="M5 8.2l2 2 4-4" fill="none" stroke="var(--green)" stroke-width="1.6"/></svg>Equity,</li>
      <li><svg class="tick" viewBox="0 0 16 16"><circle cx="8" cy="8" r="6.5" fill="none" stroke="var(--green)" stroke-width="1.6"/><path d="M5 8.2l2 2 4-4" fill="none" stroke="var(--green)" stroke-width="1.6"/></svg>Funding,</li>
      <li><svg class="tick" viewBox="0 0 16 16"><circle cx="8" cy="8" r="6.5" fill="none" stroke="var(--green)" stroke-width="1.6"/><path d="M5 8.2l2 2 4-4" fill="none" stroke="var(--green)" stroke-width="1.6"/></svg>Among other topics.</li>
    </ul>
  </section>

  <div class="footer-rule"></div>
  <footer class="footer">
    <div class="brand"><span class="brand-dot"></span><span class="brand-name">Q-TarVN</span></div>
    <span class="contact"><svg viewBox="0 0 22 22"><path d="M5 3l4 1 1 4-2 2q2 4 6 6l2-2 4 1 1 4-2 2Q9 20 3 6z" fill="none" stroke="var(--blue)" stroke-width="2"/></svg>555 010 2040</span>
    <span class="contact"><svg viewBox="0 0 22 22"><rect x="3" y="5" width="16" height="12" fill="var(--blue)"/><path d="M3 5l8 7 8-7" fill="none" stroke="#fff" stroke-width="1.5"/></svg>info@q-tarvn.com</span>
    <span class="contact"><svg viewBox="0 0 22 22"><circle cx="11" cy="11" r="8" fill="none" stroke="var(--blue)" stroke-width="2"/><ellipse cx="11" cy="11" rx="3.5" ry="8" fill="none" stroke="var(--blue)" stroke-width="1.5"/><path d="M3 11h16" stroke="var(--blue)" stroke-width="1.5"/></svg>www.q-tarvn.com</span>
  </footer>
</main>
</body>
</html>
```